依頼詳細
日時:8月5日(土) 13:30~15:00

場所:みなせ市民交流館 ポレット 会議室

定員:20名

対象:小学生以上(保護者同伴でも可能だが、実験はお子様のみで参加)

参加費:実験キット代(テキスト+ワークシート付) 1,500円
※当日、現金にて集金します。

企画:東浜日報湊西若葉会×明進桜丘教室

申込方法:QRコード、TEL、FAX

内容:鏡を使ったマジック実験をします。具体的な実験名等はないため、気の利いたタイトルを考えていただけると幸いです。参考までに実験内容の一部を添付しておきます。ちなみにキット名は、「ハンシャランド ひかりの森のキツネっす」になります。

①テキストの物語を読みながら、なぞ解きに挑戦します。実験の予想を立てましょう。
②実験キットを組み立てて、実験します。予想した結果になるか確かめます。
③科学マジックを練習します。友達と協力して、マジックのコツをつかみます。
④家に帰ったら、おうちの方や友達にマジックを披露したり、自由研究のテーマとして取り組んでみます。
※途中、先生によるマジックのデモンストレーションもあります。

また参加特典として、お子様には無料で「東浜キッズタイムズ」を3ヶ月お届けします。
保護者同伴の方には(保護者には)、珈琲工房NUVATIの水出しコーヒーをプレゼントします。

その他、ご質問等ございましたらお申し付けください。

以上、よろしくお願いいたします。
記載項目
申込書QR
TEL: 090-3842-7716 明進桜丘教室 森川
FAX: 0562-71-3048
東浜日報と明進教室ロゴ

申込書記入欄
①参加者名(ふりがなも)
②学年
③保護者名
④ご住所
⑤電話番号
サイズ
A4
ページ数
片面
希望イメージ
シンプル 複雑
単色 カラフル
暗い 明るい
日常 高級
遊び心 厳粛
未来的 伝統的
女性的 男性的
希望する色
設定なし
納品ファイル
• イラストレーター形式 (.ai)
補足説明
スクショ保存のため画質が悪いのですが、ご参考までに別の実験にはなりますが、授業中の風景もいくつか添付します。
■ 選んだ理由

子どもたちが目をひくようなイメージと配色、実験の様子なども載っており、一目見て内容が分かる点が良いと思いました。

■ 提案者全員のお礼・コメント

この度は当コンペにたくさん応募していただきありがとうございました。
どれもランサーさんの良さや個性が出ており、かなり迷ってしまいました。
ゆえに選定にお時間がかかってしまいましたことお詫び申し上げます。

今回ご縁のなかったランサーの皆様方も今後もまた別のコンペを企画する予定ですのでその時はよろしくお願いいたします。

```html
<!DOCTYPE html>
<html lang="ja">
<head>
<meta charset="utf-8">
<title>不思議な教室の魔法の鏡</title>
<link rel="stylesheet" href="https://fonts.googleapis.com/css2?family=Zen+Maru+Gothic:wght@500;700;900&family=Kaisei+Decol:wght@700&display=swap">
<style>
:root{
  --paper:#f4f1e3;
  --green:#4f9a57;
  --green-dark:#1f5230;
  --green-deep:#2f6f3c;
  --cream:#fbf6e2;
  --rose:#c8234d;
  --magenta:#8c1e58;
  --gold:#e9d27a;
  --ink:#222;
}
*{margin:0;padding:0;box-sizing:border-box}
html,body{width:857px;height:1200px;overflow:hidden;background:var(--paper)}
body{font-family:"Zen Maru Gothic",sans-serif;color:var(--ink);position:relative}
.flyer{position:absolute;inset:0}
.ornament{position:absolute}
.corner-vine-tl{left:0;top:0;width:200px;height:200px;background:radial-gradient(circle at 0 0,#c9d9b8,transparent 70%)}
.corner-vine-br{right:0;bottom:0;width:280px;height:360px;background:radial-gradient(circle at 100% 100%,#d98aa0 0,#b7ce9f 45%,transparent 72%)}
.panel{position:absolute;left:34px;top:34px;width:789px;height:1132px;background:var(--green);border:4px double var(--cream);border-radius:14px;box-shadow:0 0 0 6px var(--green-deep)}
.organiser-tag{position:absolute;right:44px;top:22px;background:#fff;padding:8px 16px;border-radius:4px;font-weight:900;font-size:20px;color:var(--green-dark)}
.tagline{position:absolute;left:200px;top:80px;font-weight:900;font-size:26px;color:#fff;letter-spacing:2px}
.title-sub{position:absolute;left:130px;top:118px;font-family:"Kaisei Decol",serif;font-size:58px;color:var(--green-dark);-webkit-text-stroke:2px #fff;paint-order:stroke fill}
.title-ruby{position:absolute;left:210px;top:190px;font-size:20px;font-weight:700;color:var(--green-dark);letter-spacing:3px}
.title-main{position:absolute;left:80px;top:212px;font-family:"Kaisei Decol",serif;font-size:128px;line-height:1;color:var(--magenta);-webkit-text-stroke:6px #fff;paint-order:stroke fill;letter-spacing:4px}
.intro{position:absolute;right:58px;top:86px;height:300px;writing-mode:vertical-rl;font-size:17px;font-weight:700;color:#fff;line-height:1.65}
.silhouette{position:absolute;left:470px;top:360px;width:290px;height:560px;border-radius:140px 140px 20px 20px;background:linear-gradient(180deg,#3c8446,#2a6334)}
.date{position:absolute;left:80px;top:440px;font-weight:900;font-size:90px;color:var(--rose);-webkit-text-stroke:5px #fff;paint-order:stroke fill}
.date small{font-size:44px}
.weekday{display:inline-block;width:50px;height:50px;border-radius:50%;background:var(--rose);color:#fff;font-size:30px;text-align:center;line-height:50px;-webkit-text-stroke:0;vertical-align:middle}
.time{position:absolute;left:120px;top:555px;font-weight:900;font-size:40px;color:#fff}
.details{position:absolute;left:80px;top:620px;width:400px;list-style:none}
.details li{display:flex;gap:10px;align-items:center;margin-bottom:10px;color:#fff;font-weight:700;font-size:16px;line-height:1.35}
.details .label{flex:none;background:var(--cream);color:var(--green-dark);font-size:14px;padding:2px 8px;border-radius:3px}
.apply{position:absolute;left:62px;top:760px;width:400px;height:270px;background:var(--cream);border-radius:10px;padding:16px 20px}
.apply h2{font-size:24px;color:var(--rose);text-align:center;margin-bottom:10px;letter-spacing:6px}
.apply p{font-size:14px;line-height:1.7;font-weight:700}
.apply .contact{margin-top:10px;font-size:17px;color:var(--green-dark)}
.perks{position:absolute;left:490px;top:930px;width:310px;color:#fff;font-weight:900;font-size:19px;line-height:1.55}
.perks em{font-style:normal;color:var(--gold)}
.perks p+p{margin-top:14px}
.organizer{position:absolute;left:62px;top:1090px;font-size:16px;font-weight:700;color:#fff}
</style>
</head>
<body>
<div class="flyer">
  <div class="ornament corner-vine-tl" role="img" aria-label="つるバラの飾り"></div>
  <div class="ornament corner-vine-br" role="img" aria-label="バラの花とつるの飾り"></div>
  <div class="panel"></div>

  <div class="organiser-tag">東浜日報・明進教室</div>

  <p class="tagline">消える!!増える!!出てくる!?</p>
  <p class="title-sub">不思議な教室の</p>
  <p class="title-ruby">〜まほうのかがみ〜</p>
  <h1 class="title-main">魔法の鏡</h1>

  <p class="intro">鏡を使った「マジック実験」。物語を読みながら謎を解き、実験で確かめよう。科学マジックを身につけて、家族や友達に披露しよう！</p>

  <div class="silhouette" role="img" aria-label="鏡を持つ少女のシルエットのイラスト"></div>

  <p class="date">8<small>月</small>5<small>日</small><span class="weekday">土</span></p>
  <p class="time">13:30〜15:00</p>

  <ul class="details">
    <li><span class="label">会場</span>みなせ市民交流館 ポレット 会議室</li>
    <li><span class="label">対象</span>小学生以上（定員20名）<br>※実験はお子様のみ</li>
    <li><span class="label">参加費</span>実験キット代 1,500円（当日現金）</li>
  </ul>

  <section class="apply">
    <h2>申込方法</h2>
    <p>お電話またはFAXで、①参加者名（ふりがな）②学年③保護者名④ご住所⑤電話番号をお知らせください。</p>
    <p class="contact">TEL 090-3842-7716<br>明進桜丘教室 森川<br>FAX 0562-71-3048</p>
  </section>

  <div class="perks">
    <p>参加特典として、お子様には無料で<em>「東浜キッズタイムズ」</em>を3ヶ月お届け!!</p>
    <p>保護者同伴の方には<em>珈琲工房NUVATI</em>の水出しコーヒーをプレゼント!</p>
  </div>

  <p class="organizer">企画：東浜日報湊西若葉会 × 明進桜丘教室</p>
</div>
</body>
</html>
```